Flat bootstrap design for existing site

I'm looking for a modern flat design based around an existing logo. This has to be a custom design (no external templates), and implemented into a bootstrap framework.

The logo is attached as 2 versions - choose whichever you want, that flows better with whatever design you choose.

Added screenshots of the existing site (currently using the default bootstrap layouts). Please make your designs around those pages in the screenshots (i.e. the homepage only has the postal code input and the header). The active page has 3 screenshots, because I wanted to illustrate the other states that would be visible (in the table rows).

This is a moving/junk removal website, just for some context.

Here's some example websites (flat designs) that I like, just to give you an idea of what I'm after.

https://www.plivoterra.com/
https://damsoqua.com/
https://trevalin.com/
https://morkadelphi.com/en/

Coding

Coded - Design and coding required

Number of Pages Required

5+ page

Colors

Designer to choose colors to be used in the design.

Requirements
Must have
• It must be a modern/simple flat design, that is built around the existing logo (attached).
• It has to be implemented using bootstrap.

```html
<!DOCTYPE html>
<html lang="en">
<head>
<meta charset="utf-8">
<title>Trundlo – Junk Removal</title>
<link rel="stylesheet" href="https://fonts.googleapis.com/css2?family=Roboto:wght@400;500;700&family=Roboto+Condensed:wght@400;700&display=swap">
<style>
:root{
  --orange:#fd6545;
  --orange-dark:#e9553a;
  --blue:#45c3f1;
  --blue-title:#36b4e9;
  --dark:#1f1f1f;
  --footer:#262626;
  --ink:#333333;
  --muted:#666666;
  --line:#dddddd;
  --field:#f1f1f1;
  --white:#ffffff;
}
*{box-sizing:border-box;margin:0;padding:0}
html,body{width:1200px;height:3136px;overflow:hidden}
body{font-family:'Roboto',sans-serif;color:var(--ink);background:var(--white);font-size:12px;line-height:1.6}
.section{position:relative;width:1200px;overflow:hidden}
.abs{position:absolute}
.heading{font-family:'Roboto Condensed',sans-serif;font-weight:700;text-transform:uppercase}
.btn{display:inline-flex;align-items:center;justify-content:center;gap:8px;background:var(--orange);color:var(--white);font-family:'Roboto Condensed',sans-serif;font-weight:700;font-size:14px;text-transform:uppercase}
.btn-arrow{width:14px;height:14px}
p.body{font-size:11.5px;line-height:19px;color:var(--muted);text-align:justify}

/* header */
.site-header{height:88px;background:var(--dark)}
.brand{left:157px;top:16px;display:flex;align-items:center;gap:12px;color:var(--blue);font-size:40px;font-weight:700;letter-spacing:1px;line-height:56px}
.brand-dot{width:22px;height:22px;border-radius:50%;background:var(--blue)}
.main-nav{right:160px;top:34px;display:flex;gap:30px}
.main-nav a{color:var(--blue);font-size:13px;font-weight:500;text-decoration:none;text-transform:uppercase}

/* hero */
.hero{height:443px}
.hero-photo{inset:0;background:linear-gradient(100deg,#5d6b3a 0%,#3d4a2c 30%,#6f7d87 55%,#8a7456 80%,#b79468 100%)}
.hero-shade{inset:0;background:rgba(0,0,0,.25)}
.hero-title{left:0;right:0;top:138px;text-align:center;color:var(--white);font-size:42px;letter-spacing:-.5px}
.postal-form{left:410px;top:228px;display:flex;height:42px}
.postal-input{width:286px;background:var(--white);color:#444;font-size:13px;padding:0 16px;display:flex;align-items:center}
.postal-btn{width:84px;background:var(--blue);color:var(--white);font-size:17px;font-weight:700;display:flex;align-items:center;justify-content:center}

/* quote band */
.quote-band{height:73px;background:var(--orange)}
.quote-band h2{left:159px;top:20px;color:var(--white);font-size:22px;font-weight:500}
.quote-band .outline-btn{left:906px;top:18px;width:132px;height:38px;border:2px solid var(--white);color:var(--white);font-size:13px;font-weight:700;text-transform:uppercase;display:flex;align-items:center;justify-content:center}

/* welcome */
.welcome{height:485px}
.callback{left:161px;top:36px;width:282px;height:395px;border:2px solid var(--orange);background:var(--white)}
.callback-head{height:52px;background:var(--orange);color:var(--white);display:flex;align-items:center;justify-content:center;gap:10px;font-size:26px}
.callback-body{padding:18px 18px 0}
.form-label{font-size:12px;color:#777}
.form-hint{font-size:9px;color:#aaa}
.radio-row{display:flex;gap:18px;margin:8px 0 14px;font-size:10px;color:#777}
.radio-row span{display:flex;align-items:center;gap:5px}
.radio{width:11px;height:11px;border:1px solid #bbb;border-radius:50%}
.field{height:28px;background:var(--field);border:1px solid #e2e2e2}
.date-field{position:relative;margin:6px 0 14px}
.date-field svg{position:absolute;right:8px;top:7px}
.name-row{display:flex;gap:12px;margin-bottom:12px}
.name-row div{flex:1}
.name-row .field{margin-top:6px}
.callback .btn{position:absolute;left:82px;bottom:18px;width:108px;height:36px}
.intro{left:506px;top:36px;width:532px}
.eyebrow{font-size:19px;color:#666;font-weight:500}
.intro h2{font-size:36px;line-height:40px;color:var(--blue-title);font-weight:700;margin:4px 0 18px}
.intro p.body{margin-bottom:16px}
.intro .btn{width:128px;height:40px;margin-top:14px}

/* services */
.services{height:439px}
.services-bg{inset:0;background:linear-gradient(120deg,#3fbaea 0%,#52c9f3 45%,#38b5e6 100%)}
.service-card{top:48px;height:268px;background:rgba(60,185,235,.95);box-shadow:0 0 0 1px rgba(255,255,255,.08);color:var(--white);text-align:center;padding:0 34px}
.service-card .icon{width:64px;height:64px;margin:42px auto 14px;border-radius:10px;background:rgba(255,255,255,.85)}
.service-card h3{font-size:20px;font-weight:700;margin-bottom:12px}
.service-card p{font-size:10.5px;line-height:16px}
.card-prep{left:163px;width:397px}
.card-collect{left:631px;width:408px}
.tagline{left:0;right:0;top:340px;text-align:center;color:var(--white);font-size:27px}
.call-line{left:0;right:0;top:382px;text-align:center;color:rgba(255,255,255,.85);font-size:23px}

/* peace of mind */
.peace{height:464px}
.peace-photo{left:161px;top:61px;width:307px;height:343px;border:4px solid #eee;background:linear-gradient(160deg,#7b4a3a 0%,#a8724f 40%,#6d5a46 70%,#c9a27b 100%)}
.peace-text{left:500px;top:48px;width:539px}
.peace-text h2{font-size:22px;color:#333;margin-bottom:10px}
.peace-text p.body{margin-bottom:10px}
.checks{list-style:none;margin-top:14px}
.checks li{display:flex;gap:12px;margin-bottom:10px}
.checks svg{flex:none;margin-top:2px}
.checks p{font-size:11.5px;line-height:17px;color:var(--muted)}
.peace-text .btn{width:112px;height:38px;margin-top:12px;font-size:12px}

/* newsletter */
.newsletter{height:216px;background:var(--orange)}
.newsletter h2{left:0;right:0;top:30px;text-align:center;color:var(--white);font-size:28px}
.newsletter p{left:270px;width:660px;top:84px;text-align:center;color:var(--white);font-size:11px;line-height:17px}
.news-form{left:161px;top:142px;display:flex;gap:12px}
.news-field{width:366px;height:34px;background:var(--white);display:flex;align-items:center;gap:10px;padding:0 12px;font-size:11px;color:#999}
.news-btn{width:122px;height:34px;background:var(--dark);color:var(--white);font-size:12px;font-weight:700;display:flex;align-items:center;justify-content:center}

/* testimonials */
.testimonials{height:405px}
.testimonials h2{left:0;right:0;top:48px;text-align:center;font-size:30px;color:#333}
.title-rule{top:68px;height:4px;border-top:1px solid #bbb;border-bottom:1px solid #bbb;width:170px}
.testimonial{top:154px;height:191px;background:var(--blue);color:var(--white);text-align:center;padding:52px 26px 0}
.testimonial .avatar{position:absolute;left:50%;top:-32px;width:72px;height:72px;margin-left:-36px;border-radius:50%;border:4px solid var(--white);background:linear-gradient(#c9a98a,#8b6c55)}
.testimonial blockquote{font-size:11px;line-height:16px;font-style:italic}
.quote-mark{font-family:Georgia,serif;font-size:26px;font-weight:700;line-height:0;vertical-align:-6px}
.testimonial cite{display:block;margin-top:16px;font-size:10px;font-style:normal}
.t1{left:161px;width:266px}.t2{left:464px;width:268px}.t3{left:771px;width:266px}

/* footer */
.site-footer{height:475px;background:linear-gradient(180deg,#2a2a2a,#1c1c1c)}
.social-eyebrow{left:0;right:0;top:36px;text-align:center;color:var(--orange);font-size:14px;font-weight:700}
.follow{left:0;right:0;top:54px;text-align:center;color:var(--white);font-size:36px}
.follow-rule{top:82px;height:4px;border-top:1px solid #666;border-bottom:1px solid #666}
.footer-intro{left:210px;width:780px;top:100px;text-align:center;color:#999;font-size:11px;line-height:17px}
.socials{left:502px;top:152px;display:flex;gap:12px}
.socials span{width:34px;height:34px;border:2px solid #ccc;border-radius:50%}
.footer-col{top:210px}
.col-eyebrow{font-size:10px;color:#bbb;text-transform:uppercase}
.footer-col h3{color:var(--white);font-size:24px;line-height:28px;margin-bottom:14px}
.footer-col p{font-size:10.5px;line-height:15px;color:#aaa}
.contact{display:flex;gap:10px;color:#ddd;font-size:11px;margin-top:14px;line-height:16px}
.contact svg{flex:none;margin-top:2px}
.about{left:159px;width:250px}
.links{left:456px;width:200px}
.links ul{list-style:none}
.links li{color:#ccc;font-size:11px;margin-bottom:10px}
.links li::before{content:"› ";color:#ccc}
.blog{left:782px;width:258px}
.post{display:flex;gap:12px;margin-bottom:22px}
.post .thumb{flex:none;width:72px;height:70px;border:3px solid #eee}
.post p{font-size:10px;line-height:14px}
.post a{display:block;color:var(--orange);font-size:9px;margin-top:14px;text-decoration:none;text-transform:uppercase}
.copyright{height:48px;background:var(--orange);color:var(--white);font-size:11px;display:flex;align-items:center;justify-content:center}
</style>
</head>
<body>

<header class="section site-header">
  <div class="abs brand"><span class="brand-dot"></span>TRUNDLO</div>
  <nav class="abs main-nav">
    <a href="#">Book</a><a href="#">How it works</a><a href="#">Become a driver</a><a href="#">Sign in</a>
  </nav>
</header>

<section class="section hero">
  <div class="abs hero-photo" role="img" aria-label="Worker loading old furniture and junk into a removal truck trailer outdoors"></div>
  <div class="abs hero-shade"></div>
  <h1 class="abs heading hero-title">Need junk removed? Book now.</h1>
  <div class="abs postal-form">
    <div class="postal-input">Postal Code</div>
    <div class="postal-btn">Book</div>
  </div>
</section>

<section class="section quote-band">
  <h2 class="abs">Looking for a quality and affordable removals service?</h2>
  <div class="abs outline-btn">Get a quote</div>
</section>

<section class="section welcome">
  <div class="abs callback">
    <div class="callback-head heading">
      <svg width="24" height="18" viewBox="0 0 24 18"><rect x="1" y="1" width="22" height="16" fill="none" stroke="#fff" stroke-width="2"/><path d="M1 1l11 9 11-9" fill="none" stroke="#fff" stroke-width="2"/></svg>
      Request a callback
    </div>
    <div class="callback-body">
      <div class="form-label">Service Category</div>
      <div class="radio-row"><span><i class="radio"></i>Junk Removal</span><span><i class="radio"></i>Moving</span><span><i class="radio"></i>Both</span></div>
      <div class="form-label">Date</div>
      <div class="form-hint">of service</div>
      <div class="date-field field"><svg width="12" height="12" viewBox="0 0 12 12"><rect x="1" y="2" width="10" height="9" fill="none" stroke="#999"/><path d="M1 5h10M4 1v2M8 1v2" stroke="#999"/></svg></div>
      <div class="name-row"><div><div class="form-label">First Name</div><div class="field"></div></div><div><div class="form-label">Last Name</div><div class="field"></div></div></div>
      <div class="name-row"><div><div class="form-label">First Name</div><div class="field"></div></div><div><div class="form-label">Last Name</div><div class="field"></div></div></div>
    </div>
    <div class="btn">Get quote</div>
  </div>
  <div class="abs intro">
    <div class="eyebrow">WELCOME TO TRUNDLO</div>
    <h2>From Planning to<br>Unpacking</h2>
    <p class="body">Lorem Ipsum is simply dummy text of the printing and typesetting industry. Lorem Ipsum has been type and scrambled it to make a type specimen book. It has survived not only five centuries, but also the leap into electronic typesetting, remaining essentially unchanged. It was popularised in the 1960s with the release of Dorraset sheets containing Lorem Ipsum passages, and more recently with desktop publishing software like Quillset Pagewright including versions of Lorem Ipsum.</p>
    <p class="body">Lorem Ipsum is simply dummy text of the printing and typesetting industry. Lorem Ipsum has been type and scrambled it to make a type specimen book. It has survived not only five centuries, but also the leap into electronic typesetting, remaining essentially unchanged. It was popularised in the 1960s with the release of Dorraset sheets containing Lorem Ipsum passages, and more recently with desktop publishing software like Quillset Pagewright including versions of Lorem Ipsum.</p>
    <div class="btn">Read more <svg class="btn-arrow" viewBox="0 0 14 14"><circle cx="7" cy="7" r="7" fill="#fff"/><path d="M5.5 4l3 3-3 3" fill="none" stroke="#fd6545" stroke-width="1.8"/></svg></div>
  </div>
</section>

<section class="section services">
  <div class="abs services-bg" role="img" aria-label="Blue tinted photo of a moving scene"></div>
  <div class="abs service-card card-prep">
    <div class="icon" role="img" aria-label="Hands holding a box icon"></div>
    <h3>Preapring</h3>
    <p>Lorem Ipsum is simply dummy text of the printing and typesetting industry. Lorem Ipsum has been type and scrambled it to make a type specimen book. It has survived not only five centuries, but also the leap into electronic typesetting, remaining essentially unchanged. It was</p>
  </div>
  <div class="abs service-card card-collect">
    <div class="icon" role="img" aria-label="Forklift with boxes icon"></div>
    <h3>Collecting</h3>
    <p>Lorem Ipsum is simply dummy text of the printing and typesetting industry. Lorem Ipsum has been type and scrambled it to make a type specimen book. It has survived not only five centuries, but also the leap into electronic typesetting, remaining essentially unchanged. It was</p>
  </div>
  <div class="abs heading tagline">Moving never can't be more easy!</div>
  <div class="abs call-line">CALL US 005518730962</div>
</section>

<section class="section peace">
  <div class="abs peace-photo" role="img" aria-label="Pile of rusty old signs, wheels and scrap junk"></div>
  <div class="abs peace-text">
    <h2 class="heading">Get peace of mind. Let us remove junk for you!</h2>
    <p class="body">Lorem Ipsum is simply dummy text of the printing and typesetting industry. Lorem Ipsum has been the industry's make a type specimen book. It has survived not only five centuries, but also the leap into electronic including versions of Lorem Ipsum.</p>
    <p class="body">Lorem Ipsum is simply dummy text of the printing and typesetting industry. Lorem Ipsum has been the industry's make a type specimen book. It has survived not only five centuries, but also the leap into electronic including versions of Lorem Ipsum.</p>
    <ul class="checks">
      <li><svg width="14" height="14" viewBox="0 0 14 14"><circle cx="7" cy="7" r="7" fill="#fd6545"/><path d="M3.8 7.2l2.2 2.2 4.2-4.4" fill="none" stroke="#fff" stroke-width="1.8"/></svg><p>Lorem Ipsum is simply dummy text of the printing and typesetting industry. specimen book. It has survived recently with desktop publishing software like Quillset Pagewright including versions of Lorem Ipsum.</p></li>
      <li><svg width="14" height="14" viewBox="0 0 14 14"><circle cx="7" cy="7" r="7" fill="#fd6545"/><path d="M3.8 7.2l2.2 2.2 4.2-4.4" fill="none" stroke="#fff" stroke-width="1.8"/></svg><p>Lorem Ipsum is simply dummy text of the printing and typesetting industry. specimen book. It has survived recently with desktop publishing software like Quillset Pagewright including versions of Lorem Ipsum.</p></li>
      <li><svg width="14" height="14" viewBox="0 0 14 14"><circle cx="7" cy="7" r="7" fill="#fd6545"/><path d="M3.8 7.2l2.2 2.2 4.2-4.4" fill="none" stroke="#fff" stroke-width="1.8"/></svg><p>Lorem Ipsum is simply dummy text of the printing and typesetting industry. specimen book. It has survived recently with desktop publishing software like Quillset Pagewright including versions of Lorem Ipsum.</p></li>
    </ul>
    <div class="btn">Read more <svg class="btn-arrow" viewBox="0 0 14 14"><circle cx="7" cy="7" r="7" fill="#fff"/><path d="M5.5 4l3 3-3 3" fill="none" stroke="#fd6545" stroke-width="1.8"/></svg></div>
  </div>
</section>

<section class="section newsletter">
  <h2 class="abs heading">Sign up for newsletter</h2>
  <p class="abs">Lorem Ipsum is simply dummy text of the printing and typesetting industry. Lorem Ipsum has been the industry's standard dummy text ever since when an unknown printer took.</p>
  <div class="abs news-form">
    <div class="news-field"><svg width="12" height="12" viewBox="0 0 12 12"><circle cx="6" cy="4" r="2.6" fill="#999"/><path d="M1 12c0-3 2.2-5 5-5s5 2 5 5z" fill="#999"/></svg>Enter Your Name</div>
    <div class="news-field"><svg width="13" height="10" viewBox="0 0 13 10"><rect width="13" height="10" fill="#999"/><path d="M0 0l6.5 5L13 0" fill="none" stroke="#fff"/></svg>Enter Your Email</div>
    <div class="news-btn">SUBSCRIBE NOW!</div>
  </div>
</section>

<section class="section testimonials">
  <div class="abs title-rule" style="left:340px"></div>
  <div class="abs title-rule" style="left:690px"></div>
  <h2 class="abs heading">Testimonial</h2>
  <div class="abs testimonial t1">
    <div class="avatar" role="img" aria-label="Customer portrait"></div>
    <blockquote><span class="quote-mark">“</span> scrambled it to make a type also Dorraset sheets containing Lorem Ipsum passages, and more recently with desktop publishing software like Quillset Pagewright including versions of Lorem Ipsum <span class="quote-mark">”</span></blockquote>
    <cite>— Daniel Morrow</cite>
  </div>
  <div class="abs testimonial t2">
    <div class="avatar" role="img" aria-label="Customer portrait"></div>
    <blockquote><span class="quote-mark">“</span> scrambled it to make a type also Dorraset sheets containing Lorem Ipsum passages, and more recently with desktop publishing software like Quillset Pagewright including versions of Lorem Ipsum <span class="quote-mark">”</span></blockquote>
    <cite>— Lena Vale</cite>
  </div>
  <div class="abs testimonial t3">
    <div class="avatar" role="img" aria-label="Customer portrait"></div>
    <blockquote><span class="quote-mark">“</span> scrambled it to make a type also Dorraset sheets containing Lorem Ipsum passages, and more recently with desktop publishing software like Quillset Pagewright including versions of Lorem Ipsum <span class="quote-mark">”</span></blockquote>
    <cite>— Daniel Morrow</cite>
  </div>
</section>

<footer class="section site-footer">
  <div class="abs social-eyebrow">SOCIAL PROFILES</div>
  <div class="abs follow-rule" style="left:170px;width:330px"></div>
  <div class="abs follow-rule" style="left:700px;width:350px"></div>
  <h2 class="abs heading follow">Follow us</h2>
  <p class="abs footer-intro">Lorem Ipsum is simply dummy text of the printing and typesetting industry. Lorem Ipsum has been the industry's standard dummy text ever since the 1500s, when an unknown printer took a galley of type and scrambled it to make a type specimen book.</p>
  <div class="abs socials"><span></span><span></span><span></span><span></span><span></span></div>

  <div class="abs footer-col about">
    <div class="col-eyebrow">Shortly</div>
    <h3 class="heading">About us</h3>
    <p>Lorem Ipsum is simply dummy text of the printing and unknown printer took a galley of type and scrambled it to make a type specimen good text book.</p>
    <div class="contact"><svg width="13" height="10" viewBox="0 0 13 10"><rect width="13" height="10" fill="#ddd"/><path d="M0 0l6.5 5L13 0" fill="none" stroke="#262626"/></svg>hello@trundlo.com</div>
    <div class="contact"><svg width="12" height="12" viewBox="0 0 12 12"><path d="M2.5 1l2 2.5-1.2 1.3a7 7 0 0 0 3.9 3.9L8.5 7.5 11 9.5 9.8 11C5 11 1 7 1 2.2z" fill="#ddd"/></svg>P: (562) 318-4490</div>
    <div class="contact"><svg width="10" height="14" viewBox="0 0 10 14"><path d="M5 0a5 5 0 0 0-5 5c0 4 5 9 5 9s5-5 5-9a5 5 0 0 0-5-5z" fill="#ddd"/><circle cx="5" cy="5" r="1.8" fill="#262626"/></svg>Brightwater Ridge 4120 - 215 Alder Hollow Drive SE Redvale, Northmere</div>
  </div>

  <div class="abs footer-col links">
    <div class="col-eyebrow">Our</div>
    <h3 class="heading">Quick links</h3>
    <ul><li>Home</li><li>Book</li><li>How it works</li><li>Become a Driver</li><li>Sign in</li><li>Contact Us</li></ul>
  </div>

  <div class="abs footer-col blog">
    <div class="col-eyebrow">Recent</div>
    <h3 class="heading">Blog</h3>
    <div class="post"><div class="thumb" role="img" aria-label="Blog post photo of movers with boxes" style="background:linear-gradient(135deg,#9c7a5a,#d8c2a0)"></div><div><p>Lorem Ipsum is simply dummy text of the printing industry. Lorem Ipsum has been the industry's standard</p><a href="#">Read more</a></div></div>
    <div class="post"><div class="thumb" role="img" aria-label="Blog post photo of scrap junk pile" style="background:linear-gradient(135deg,#7b4a3a,#b88a64)"></div><div><p>Lorem Ipsum is simply dummy text of the printing industry. Lorem Ipsum has been the industry's standard</p><a href="#">Read more</a></div></div>
  </div>
</footer>

<div class="copyright">© 2017 trundlo. All rights reserved.</div>

</body>
</html>
```